Need App for Impact Related Events

My app is to help with internal events. When you enter the prompted event code the next screen shows you everyone currently at the event. It will give you the ability to Start a conversation with someone you met at that event, or signal it is your turn to send a message. The next screen is a message thread with that person. I am looking for a design that incorporates the colors and ‘feel good’ emotion of our logo. I have pieced together a pretty good interpretation of what I’m looking for in the attached mockup by slicing and dicing designs. I also attached our logo mascot.Screens (see attached mockups)

Note 1: I do not like the picture on the screen used in screen one because it makes it seem like a dating app. I attached an alternative photo that can be used or present different ideas.

Note 2: On the login/signup screen (screen 2) I need an additional first and last name for login, you can try to fit this on one login screen or present a two step signup screen where that is presented in the second screen.

READ MOCKUP GUIDELINES UNDER Must Haves

Target Market(s)

People attending internal social impact events

Industry/Entity Type

Charity

Font styles to use
Sans Serif

Colors
86cfc6

Requirements
Must have
• Follow the screen mockups attached to project
• PLEASE READ
• I have provided a relatively close design of what I’m looking for in the mockups. Some screens need to be followed more closely to my design mockup than other. I have listed a guide below how how closely you should follow my mockup design exactly. Overall I would like to see some ideas of incorporating a few accent colors so it doesn’t appear SO Blue. I also attached some app inspiration designs I found from around the web
• Screen Mockup Guideline Follow %
• Screen 1: 65% - mostly on target, would like to see ways to make it not SO Blue and possibly creative places to add some explainer text describing the app
• Screen 2: 50% - general design idea is here, but more open
• Screen 3: 35% - a lot more room for design influence
• Screen 4: 70% - mostly on target, a little room for design influence/color scheme ideas
• Screen 5-6: 25% - a lot of room for design change/ideas/influence
• Screen 7-8: 80% - already very close to what I need, maybe open to slight sizing and color scheme ideas
• Screen 9: 15% - the most open for influence, only the general functionality of the screen is communicated here
Nice to have
• Please Read Mockup Guideline above. In large part I am looking for something to use some nice accent colors so it is not overwhelmingly blue and bring the whole design into a seamless style.
Should not have

```html
<!DOCTYPE html>
<html lang="en">
<head>
<meta charset="UTF-8">
<title>Sign up</title>
<link href="https://fonts.googleapis.com/css2?family=Nunito+Sans:wght@400;600;700;800;900&display=swap" rel="stylesheet">
<style>
  :root {
    --bg: #ffffff;
    --ink: #22222e;
    --field-text: #3c3c4a;
    --muted: #6e6e7c;
    --field-border: #e4e4ea;
    --brand-teal: #86cfc6;
    --brand-teal-deep: #4aa89d;
    --brand-teal-text: #2f8f85;
    --shadow: rgba(74, 168, 157, 0.32);
  }
  * { box-sizing: border-box; margin: 0; padding: 0; }
  html, body {
    width: 675px;
    height: 1200px;
    overflow: hidden;
    background: var(--bg);
    font-family: "Nunito Sans", sans-serif;
    color: var(--ink);
  }
  .screen {
    position: relative;
    width: 675px;
    height: 1200px;
  }
  .back-button {
    position: absolute;
    left: 38px;
    top: 50px;
    width: 34px;
    height: 34px;
  }
  .title {
    position: absolute;
    left: 58px;
    top: 152px;
    font-size: 58px;
    font-weight: 900;
    letter-spacing: 0.5px;
  }
  .signup-form {
    position: absolute;
    left: 58px;
    top: 330px;
    width: 556px;
  }
  .field-row {
    display: flex;
    gap: 20px;
    margin-bottom: 45px;
  }
  .field-row .field { flex: 1; margin-bottom: 0; }
  .field {
    position: relative;
    height: 72px;
    border: 2px solid var(--field-border);
    border-radius: 8px;
    display: flex;
    align-items: center;
    padding: 0 26px;
    margin-bottom: 45px;
    font-size: 28px;
    font-weight: 600;
    color: var(--field-text);
    letter-spacing: 0.4px;
    white-space: nowrap;
    overflow: hidden;
  }
  .field--password {
    margin-bottom: 0;
    letter-spacing: 7px;
    font-weight: 700;
    font-size: 26px;
    padding-top: 8px;
  }
  .visibility-toggle {
    position: absolute;
    right: 34px;
    top: 50%;
    transform: translateY(-50%);
    width: 34px;
    height: 34px;
  }
  .submit-button {
    position: absolute;
    left: 512px;
    top: 729px;
    width: 102px;
    height: 102px;
    border-radius: 50%;
    background: linear-gradient(135deg, var(--brand-teal) 0%, var(--brand-teal-deep) 100%);
    box-shadow: 0 8px 20px var(--shadow);
    display: flex;
    align-items: center;
    justify-content: center;
  }
  .login-prompt {
    position: absolute;
    left: 0;
    right: 0;
    top: 1050px;
    text-align: center;
    font-size: 26px;
    color: var(--muted);
    letter-spacing: 0.3px;
  }
  .login-prompt .login-link { color: var(--brand-teal-text); font-weight: 800; }
</style>
</head>
<body>
  <main class="screen">
    <svg class="back-button" viewBox="0 0 34 34" aria-label="Back">
      <polyline points="22,4 9,17 22,30" fill="none" stroke="var(--ink)" stroke-width="3" stroke-linecap="round" stroke-linejoin="round"/>
    </svg>

    <h1 class="title">Sign up</h1>

    <form class="signup-form">
      <div class="field-row">
        <div class="field field--first-name">Daniel</div>
        <div class="field field--last-name">Foster</div>
      </div>
      <div class="field field--email">danfost@samplemail.com</div>
      <div class="field field--password">
        ********
        <svg class="visibility-toggle" viewBox="0 0 34 34" aria-label="Show password">
          <circle cx="17" cy="18" r="11" fill="none" stroke="var(--brand-teal-deep)" stroke-width="3.2"/>
          <line x1="5" y1="31" x2="29" y2="4" stroke="var(--brand-teal-deep)" stroke-width="3.2" stroke-linecap="round"/>
        </svg>
      </div>
    </form>

    <div class="submit-button" role="button" aria-label="Continue">
      <svg width="46" height="30" viewBox="0 0 46 30">
        <line x1="3" y1="15" x2="42" y2="15" stroke="#fff" stroke-width="3.6" stroke-linecap="round"/>
        <polyline points="30,3 42,15 30,27" fill="none" stroke="#fff" stroke-width="3.6" stroke-linecap="round" stroke-linejoin="round"/>
      </svg>
    </div>

    <p class="login-prompt">Already have an account? <span class="login-link">Login</span></p>
  </main>
</body>
</html>
```